Concierge Healthcare Business Card Design and Logo

We need a logo and business card design for a new company called "Sound Keeper". We will provide concierge audiological care, hearing aids, hearing exams, custom hearing protection etc to patients in the comfort of their homes and offices. We would like a sleek and modern design preferably with an Ear related logo.

Target Market(s)

People with hearing loss, Hunters, Musicians
My usual clientele are older individuals so usually 50+ years old

Industry/Entity Type

Health Care

Contact Information for Business Card

Clara Whitfield, AuD
Audiologist
512-418-2967
soundkeeper@mailvista.net
www.soundkeeperclinic.net

Logo Text

Sound Keeper

Number of Pages Required

3 page

```html
<!DOCTYPE html>
<html lang="en">
<head>
<meta charset="utf-8">
<title>Sound Keeper – Business Card</title>
<link rel="stylesheet" href="https://fonts.googleapis.com/css2?family=Libre+Caslon+Text:wght@400&family=Montserrat:wght@400&display=swap">
<style>
  :root {
    --backdrop: #dcdde0;
    --card: #ffffff;
    --ink-gray: #8f8f92;
    --rule-gray: #b9babd;
    --purple: #5e4a9f;
    --blue: #34a7df;
    --icon-cyan: #22a9e6;
    --serif: "Libre Caslon Text", Georgia, serif;
    --sans: "Montserrat", Arial, sans-serif;
  }
  * { margin: 0; padding: 0; box-sizing: border-box; }
  html, body { width: 1011px; height: 1200px; overflow: hidden; background: var(--backdrop); }
  .sheet { position: relative; width: 1011px; height: 1200px; }

  .card {
    position: absolute; left: 124px; width: 763px; height: 435px;
    background: var(--card); border-radius: 34px; overflow: hidden;
    box-shadow: 0 3px 18px rgba(0,0,0,0.16);
  }
  .card--front { top: 124px; }
  .card--back { top: 641px; }

  .front-mark { position: absolute; left: -70px; top: 20px; width: 300px; height: 300px; }

  .wordmark { font-family: var(--serif); color: var(--ink-gray); font-weight: 400; white-space: nowrap; letter-spacing: -0.5px; }
  .tagline {
    display: flex; align-items: center; gap: 8px;
    font-family: var(--sans); color: var(--ink-gray); white-space: nowrap;
  }
  .tagline::before, .tagline::after {
    content: ""; flex: 1; height: 2px;
    background: linear-gradient(90deg, transparent, var(--ink-gray) 40%, var(--ink-gray) 60%, transparent);
  }

  .front-brand { position: absolute; left: 303px; top: 270px; width: 430px; text-align: center; }
  .front-brand .wordmark { font-size: 60px; line-height: 70px; }
  .front-brand .tagline { font-size: 26px; margin-top: 2px; }
  .front-brand .site { font-family: var(--sans); font-size: 19px; color: var(--ink-gray); margin-top: 18px; letter-spacing: 0.3px; }

  .back-brand { position: absolute; left: 44px; top: 110px; width: 300px; text-align: center; }
  .back-brand .dot { width: 70px; height: 70px; border-radius: 50%; margin: 0 auto 22px;
    background: linear-gradient(180deg, var(--purple), var(--blue)); }
  .back-brand .wordmark { font-size: 39px; line-height: 46px; }
  .back-brand .tagline { font-size: 18px; margin-top: 0; }

  .divider { position: absolute; left: 379px; top: 69px; width: 2px; height: 298px; background: var(--rule-gray); }

  .contact { position: absolute; left: 414px; top: 164px; }
  .contact .person { font-family: var(--serif); font-size: 25px; color: var(--purple); }
  .contact .role { font-family: var(--sans); font-size: 17px; color: var(--ink-gray); letter-spacing: 0.5px; margin-top: 6px; }
  .contact .lines { margin-top: 22px; list-style: none; }
  .contact .lines li { display: flex; align-items: center; gap: 7px; font-family: var(--sans); font-size: 19.5px; color: var(--ink-gray); line-height: 25px; }
  .contact .lines svg { width: 16px; height: 16px; fill: var(--icon-cyan); flex: none; }
</style>
</head>
<body>
<div class="sheet">
  <section class="card card--front">
    <svg class="front-mark" viewBox="0 0 300 300" aria-hidden="true">
      <defs>
        <linearGradient id="markFade" x1="0" y1="0" x2="0" y2="1">
          <stop offset="0" stop-color="#5e4a9f"/>
          <stop offset="1" stop-color="#34a7df"/>
        </linearGradient>
      </defs>
      <circle cx="150" cy="150" r="150" fill="url(#markFade)"/>
    </svg>
    <div class="front-brand">
      <div class="wordmark">Sound Keeper</div>
      <div class="tagline">Tageline Goes Here</div>
      <div class="site">www.SoundKeeperClinic.net</div>
    </div>
  </section>

  <section class="card card--back">
    <div class="back-brand">
      <div class="dot"></div>
      <div class="wordmark">Sound Keeper</div>
      <div class="tagline">Tageline Goes Here</div>
    </div>
    <div class="divider"></div>
    <div class="contact">
      <div class="person">Clara Whitfield, AuD</div>
      <div class="role">AUDIOLOGIST</div>
      <ul class="lines">
        <li>
          <svg viewBox="0 0 24 24" aria-hidden="true"><path d="M6.6 10.8a15.1 15.1 0 0 0 6.6 6.6l2.2-2.2a1 1 0 0 1 1-.25 11.4 11.4 0 0 0 3.6.6 1 1 0 0 1 1 1V20a1 1 0 0 1-1 1A17 17 0 0 1 3 4a1 1 0 0 1 1-1h3.5a1 1 0 0 1 1 1c0 1.25.2 2.45.6 3.6a1 1 0 0 1-.25 1z"/></svg>
          512-418-2967
        </li>
        <li>
          <svg viewBox="0 0 24 24" aria-hidden="true"><path d="M2 5h20v14H2z" opacity="0.9"/><path d="M2 5l10 8 10-8" fill="none" stroke="#fff" stroke-width="2"/></svg>
          soundkeeper@mailvista.net
        </li>
      </ul>
    </div>
  </section>
</div>
</body>
</html>
```